New Business Card Design for Business Consulting Business

We need a business card design that reflects the simplicity of our business. We partner with our clients to help them deliver change. We are a different kind of business consulting group. We don't just provide you with the theory. We provide you with the leadership and capability to execute change.

Vonduro is a professional services organisation that partners with their clients to lead the execution of strategic process and system improvement initiatives. Vonduro combines hands on delivery with coaching in best practice methodologies and approaches to build their clients capabilities to ensure their ongoing success in project implementations. Vonduro offers business advisory services in Project Management, Business Process Management, Change Management and Business Analytics.

Reason: Hi Designers, Thanks for all of your great designs. There are some really creative and cool ideas. Everyone is really capturing the essence of my business Vonduro. I am extending the deadline for the business card design by 6 days as I need to consult my Marketing colleague who won't be back in Australia until Wednesday. I would like to sit down with them and review all of the best designs. The key themes of the things I have really liked on my first review are: 1) Capturing the company website on the back of the card. 2) Including the company logo on the back of the card too. 3) Including the types of services on the back of the card that the company offers - Project Management - Business Process Management - Change Management - Business Analytics 4) Utilising some images on the back of the card Just so everyone knows the colour palette for the Vonduro company logo is: R: 0 G: 86 B: 162 or C: 97% M: 73% Y: 4% K: 0% Thanks Gareth

Hi Designers,

Thanks for all of your submissions to date.  I am working through each design and will provide feedback on all the great work.

One thing I would like to ask is if you could submit a version that has my academic credentials under or after my name.  I am not a big fan of doing this but as I am in business consulting it does seem to be quite common.

I hold a Bachelor of Commerce (BCom) and a Master of Business Administration (MBA)

Thanks

Gareth

Hi Designers,

Thanks for all of your fantastic designs.  There are some really great designs here for my business.  I am still in the process of reviewing designs and should have this completed by tomorrow.  Some of the things I have learnt from this round of designs are:

1) I prefer to have the card without my academic qualifications

2) I really like cards that have a blue back

3) I prefer to have my name and title either left or right of centre

I hope this helps and I will endeavour to get through all of the designs tomorrow

Cheers

Gareth

Target Market(s)

We target large corporate organisations

Industry/Entity Type

Leadership

Requirements
Must have
• Must have the following business details

Gareth Pilling - Director
Address: Level 7, 82 Harlow Street, Melbourne, Australia, 3000
Phone: +61 3 527 840 213
Fax: +61 3 9214 5037
Email: gareth.pilling@vonduro-example.com.au
LinkedIn: au.linkedin.com/in/garethjpilling/
Twiiter: @garethjpilling
Website: www.vonduro-example.com.au

```html
<!DOCTYPE html>
<html lang="en">
<head>
<meta charset="utf-8">
<title>Vonduro Business Card</title>
<link rel="stylesheet" href="https://fonts.googleapis.com/css2?family=Lato:wght@400;700&display=swap">
<style>
  :root {
    --brand-blue: #0056a2;
    --card-white: #ffffff;
    --ink: #1d1d1f;
    --backdrop: #2a2b2d;
  }
  * { box-sizing: border-box; margin: 0; padding: 0; }
  html, body { width: 1200px; height: 926px; overflow: hidden; }
  body {
    background: var(--backdrop);
    font-family: 'Lato', sans-serif;
    position: relative;
  }
  .card {
    position: absolute;
    left: 250px;
    width: 700px;
    height: 400px;
    background: var(--card-white);
    overflow: hidden;
  }
  .card--back { top: 42px; }
  .card--front { top: 484px; }

  /* back */
  .back-logo {
    position: absolute;
    left: 0; right: 0; top: 156px;
    text-align: center;
    color: var(--brand-blue);
    font-weight: 400;
    font-size: 76px;
    line-height: 1;
    letter-spacing: 1px;
  }

  /* front */
  .front-panel { position: absolute; left: 0; top: 0; }
  .front-stripe {
    position: absolute; right: 0; top: 0;
    width: 28px; height: 100%;
    background: var(--brand-blue);
  }
  .front-logo {
    position: absolute; left: 34px; top: 82px;
    color: var(--card-white);
    font-size: 44px; font-weight: 400;
    line-height: 1;
  }
  .socials {
    position: absolute; left: 34px; top: 300px;
    color: var(--card-white);
    font-size: 15px;
    list-style: none;
  }
  .socials li { display: flex; align-items: center; gap: 10px; margin-bottom: 12px; }
  .social-mark { width: 16px; height: 16px; border-radius: 50%; background: var(--card-white); }

  .identity {
    position: absolute; right: 72px; top: 138px;
    text-align: right;
  }
  .identity__name { color: var(--brand-blue); font-weight: 700; font-size: 30px; }
  .identity__title { color: var(--ink); font-size: 13px; letter-spacing: 4px; margin-top: 2px; }

  .contacts {
    position: absolute; left: 340px; top: 222px;
    list-style: none;
    color: var(--ink); font-size: 15px; line-height: 22px;
  }
  .contacts b { color: var(--brand-blue); font-weight: 700; display: inline-block; width: 22px; }
  .contacts .indent { padding-left: 22px; }
</style>
</head>
<body>
  <section class="card card--back" aria-label="Card back">
    <div class="back-logo">Vonduro</div>
  </section>

  <section class="card card--front" aria-label="Card front">
    <svg class="front-panel" width="340" height="400" viewBox="0 0 340 400">
      <path d="M0 0 H305 V92 L322 104 L305 114 V400 H0 Z" fill="var(--brand-blue)"/>
    </svg>
    <div class="front-stripe"></div>

    <div class="front-logo">Vonduro</div>

    <ul class="socials">
      <li><span class="social-mark"></span>au.linkedin.com/in/garethjpilling/</li>
      <li><span class="social-mark"></span>@garethjpilling</li>
    </ul>

    <div class="identity">
      <div class="identity__name">Gareth Pilling</div>
      <div class="identity__title">DIRECTOR</div>
    </div>

    <ul class="contacts">
      <li><b>A</b>: Level 7, 82 Harlow Street,</li>
      <li class="indent">Melbourne, Australia, 3000</li>
      <li><b>P</b>: +61 3 527 840 213</li>
      <li><b>F</b>: +61 3 9214 5037</li>
      <li><b>w</b>: www.vonduro-example.com.au</li>
      <li><b>E</b>: gareth.pilling@vonduro-example.com.au</li>
    </ul>
  </section>
</body>
</html>
```